Business Card Design needed for start up company Pramora

In need of a new business card designed for a start up company based in Sydney, Pramora is a new start up innovative Company, our mission it to make property accessible for everyday Australian and to become the leading Real Estate platform in Australia. We want it to be fresh and clean.

Industry/Entity Type

Financial

Contact Information for Business Card

Section for Name
Section for Title

PRAMORA - Where Doors Open Wide
Mobile:
Direct:

Font styles to use
Sans Serif

Colors
33a6d7
0692cd
0255a3
ffffff

Requirements
Must have
• Logo, all business card details

```html
<!DOCTYPE html>
<html lang="en">
<head>
<meta charset="utf-8">
<title>Pramora Business Card</title>
<link rel="stylesheet" href="https://fonts.googleapis.com/css2?family=Oswald:wght@500&family=Open+Sans:wght@400;600&display=swap">
<style>
  :root {
    --bg: #e6e8eb;
    --card-dark: #2a2a2c;
    --card-dark-text: #c9c9cc;
    --card-light: #ffffff;
    --ink: #333336;
    --ink-soft: #555559;
    --brand-blue: #0255a3;
    --rule: #555559;
  }
  * { box-sizing: border-box; margin: 0; padding: 0; }
  html, body {
    width: 1200px; height: 1000px; overflow: hidden;
    background: var(--bg);
    font-family: "Open Sans", Arial, sans-serif;
  }
  .stage { position: relative; width: 1200px; height: 1000px; }
  .card {
    position: absolute; left: 280px;
    width: 640px; height: 366px;
    box-shadow: 0 6px 20px rgba(0,0,0,.18);
  }
  .card--back { top: 70px; background: var(--card-dark); }
  .card--front { top: 520px; background: var(--card-light); }

  .back-wordmark {
    position: absolute; left: 0; right: 0; top: 145px;
    text-align: center;
    font-weight: 600; font-size: 58px; letter-spacing: 2px;
    color: var(--card-dark-text);
  }

  .identity {
    position: absolute; right: 370px; top: 126px; text-align: right;
  }
  .identity__name {
    font-family: "Oswald", "Arial Narrow", sans-serif;
    font-weight: 500; font-size: 34px; letter-spacing: 1px;
    color: var(--ink); line-height: 1.1;
  }
  .identity__title {
    font-weight: 600; font-size: 19px; color: var(--brand-blue);
    letter-spacing: .5px;
  }
  .divider {
    position: absolute; left: 290px; top: 124px;
    width: 1px; height: 84px; background: var(--rule);
  }
  .contacts {
    position: absolute; left: 312px; top: 126px;
    list-style: none;
  }
  .contacts__item {
    display: flex; align-items: center; gap: 12px;
    font-size: 16px; color: var(--ink-soft); height: 21px;
  }
  .contacts__item svg { width: 13px; height: 13px; fill: var(--brand-blue); flex: none; }
  .contacts__accent { color: var(--brand-blue); }

  .footer {
    position: absolute; left: 22px; bottom: 52px;
    display: flex; align-items: baseline; gap: 8px;
    font-size: 16px; color: var(--ink-soft); letter-spacing: .5px;
  }
  .footer__wordmark {
    font-weight: 600; font-size: 16px; color: var(--brand-blue);
  }
</style>
</head>
<body>
<main class="stage">
  <section class="card card--back" aria-label="Card back">
    <p class="back-wordmark">PRAMORA</p>
  </section>

  <section class="card card--front" aria-label="Card front">
    <div class="identity">
      <p class="identity__name">LUCAS HART</p>
      <p class="identity__title">Director</p>
    </div>
    <div class="divider"></div>
    <ul class="contacts">
      <li class="contacts__item">
        <svg viewBox="0 0 16 16"><path d="M3 1l3 3-2 2c1 2 3 4 5 5l2-2 3 3-2 3C6 15 1 10 0 3z"/></svg>
        000 123 456 789
      </li>
      <li class="contacts__item">
        <svg viewBox="0 0 16 16"><path d="M4 0h8v16H4zM5.5 2v10h5V2zM7 13h2v1.5H7z" fill-rule="evenodd"/></svg>
        000 222 3334
      </li>
      <li class="contacts__item">
        <svg viewBox="0 0 16 16"><path d="M0 3h16v10H0zM1.5 4.5L8 9l6.5-4.5z" fill-rule="evenodd"/></svg>
        urname@email.com
      </li>
      <li class="contacts__item">
        <svg viewBox="0 0 16 16"><circle cx="8" cy="8" r="7.5"/><path d="M0.5 8h15M8 0.5v15" stroke="#fff" stroke-width="1"/><ellipse cx="8" cy="8" rx="3" ry="7.5" fill="none" stroke="#fff" stroke-width="1"/></svg>
        <span>www.<span class="contacts__accent">websitename</span>.com</span>
      </li>
    </ul>
    <div class="footer">
      <span class="footer__wordmark">PRAMORA</span>
      <span>- Your Street Address, Sydney, 1234</span>
    </div>
  </section>
</main>
</body>
</html>
```